Energy trading company (Voltrisa) needs a business card

We need a business card for a company based in Central America. Our main purpose is trading energy . We already have the logo but we need some good creativity to design a high impact business card. Colors blue, orange, green can be used or we would like to see good combinatios with our logo

Target Market(s)

Energy

Industry/Entity Type

Power Generation

Contact Information for Business Card

Logo , headquarters , name, background

Font styles to use
Serif
Sans Serif

Colors

Designer to choose colors to be used in the design.

Requirements
Must have
• it must have a fresh and clean view
Nice to have
• good backgrounds that combine with the logo
Should not have
• too much words

```html
<!DOCTYPE html>
<html lang="en">
<head>
<meta charset="utf-8">
<title>Voltrisa – Business Card</title>
<link rel="stylesheet" href="https://fonts.googleapis.com/css2?family=Lato:wght@400;700&display=swap">
<style>
  :root {
    --orange: #f28c1c;
    --orange-light: #f6a54e;
    --orange-pale: rgba(248, 196, 138, 0.55);
    --ink: #1e1e1e;
    --grey-text: #6b6b6b;
    --stage: #e4e4e4;
    --paper: #ffffff;
  }
  * { margin: 0; padding: 0; box-sizing: border-box; }
  html, body {
    width: 1200px; height: 912px; overflow: hidden;
    background: var(--stage);
    font-family: "Lato", Arial, sans-serif;
  }
  .canvas { position: relative; width: 1200px; height: 912px; }
  .card {
    position: absolute; width: 560px; height: 320px; overflow: hidden;
    box-shadow: 0 6px 18px rgba(0,0,0,0.18);
  }
  .card--front { left: 60px; top: 130px; background: var(--paper); }
  .card--back { left: 580px; top: 470px; background: var(--orange); }

  .card__wash { position: absolute; inset: 0; }
  .card--front .card__wash {
    background:
      linear-gradient(to bottom, var(--orange-pale) 0%, rgba(255,255,255,0) 16%),
      linear-gradient(160deg, rgba(255,255,255,0) 55%, var(--orange-pale) 82%, rgba(242,140,28,0.75) 100%);
  }
  .card--back .card__wash {
    background: linear-gradient(160deg, var(--orange) 0%, var(--orange-light) 55%, var(--orange) 100%);
  }

  .person { position: absolute; left: 46px; top: 92px; }
  .person__name { font-size: 24px; font-weight: 700; color: var(--ink); }
  .person__role { font-size: 13px; color: var(--orange); margin-top: 2px; }

  .address { position: absolute; left: 52px; top: 170px; font-size: 13.5px; line-height: 22px; color: var(--grey-text); font-style: normal; }

  .contacts { position: absolute; left: 62px; top: 236px; list-style: none; font-size: 13.5px; color: var(--grey-text); }
  .contacts li { display: flex; align-items: center; height: 21px; }
  .contacts svg { width: 11px; height: 11px; margin-right: 10px; fill: var(--orange); }

  .brand { position: absolute; display: flex; flex-direction: column; align-items: center; }
  .brand__dot { width: 34px; height: 34px; border-radius: 50%; margin-bottom: 8px; }
  .brand__name { font-weight: 400; letter-spacing: 1px; }
  .card--front .brand { left: 360px; top: 72px; width: 180px; }
  .card--front .brand__dot { background: var(--orange); }
  .card--front .brand__name { font-size: 28px; color: var(--orange); }
  .card--back .brand { left: 300px; top: 108px; width: 200px; }
  .card--back .brand__dot { background: var(--paper); width: 40px; height: 40px; }
  .card--back .brand__name { font-size: 32px; color: var(--paper); }
</style>
</head>
<body>
<main class="canvas">

  <section class="card card--front" aria-label="Business card front">
    <div class="card__wash" role="img" aria-label="Soft orange wave decoration along the top and lower right"></div>

    <div class="person">
      <h1 class="person__name">Your Name</h1>
      <p class="person__role">Director</p>
    </div>

    <address class="address">
      214 Corriente Ave. 3B -118<br>
      Lumen, CR 40217
    </address>

    <ul class="contacts">
      <li><svg viewBox="0 0 24 24"><path d="M6.6 10.8a15.1 15.1 0 0 0 6.6 6.6l2.2-2.2c.3-.3.7-.4 1-.2 1.1.4 2.3.6 3.6.6.6 0 1 .4 1 1V20c0 .6-.4 1-1 1A17 17 0 0 1 3 4c0-.6.4-1 1-1h3.5c.6 0 1 .4 1 1 0 1.3.2 2.5.6 3.6.1.3 0 .7-.2 1z"/></svg>506.402.7731</li>
      <li><svg viewBox="0 0 24 24"><path d="M2 5h20v2l-10 6L2 7z M2 9l10 6 10-6v10H2z"/></svg>contact@voltrisa.example</li>
      <li><svg viewBox="0 0 24 24"><circle cx="12" cy="12" r="10"/></svg>www.voltrisa.example</li>
    </ul>

    <div class="brand">
      <span class="brand__dot"></span>
      <span class="brand__name">VOLTRISA</span>
    </div>
  </section>

  <section class="card card--back" aria-label="Business card back">
    <div class="card__wash" role="img" aria-label="Textured orange background with light wave decoration"></div>

    <div class="brand">
      <span class="brand__dot"></span>
      <span class="brand__name">VOLTRISA</span>
    </div>
  </section>

</main>
</body>
</html>
```